RLB Stationary
CEO Business Card
RLB Stationary -
Use specific fonts
Use same logo font or complimentary fonts to logo
Professional
Dale Vorrinth
CEO
3187 Tollgate Fern Ct., #412 Brennick Falls, OH 44821
Dale@HollowbrookUpkeep.com
www.hollowbrookupkeep.com
We are a commercial construction company who's clients are premiere property management companies. Our presence should connote corporate strength and confidence. Our colors are gray and blue.
Services provided. General Facilities Management Build-Outs Carpentry Painting Drywall Ceramic Tile Masonry Concrete Tuck & Point Pavers Awnings Ceiling Tile Power Washing Graffiti Removal Doors & Windows Flood Remediation Apartment Turns & Much More

```html
<!DOCTYPE html>
<html lang="en">
<head>
<meta charset="utf-8">
<title>RLB Stationery Set</title>
<link href="https://fonts.googleapis.com/css2?family=Montserrat:wght@400;600;800&display=swap" rel="stylesheet">
<style>
  :root {
    --navy: #1f3a6b;
    --gray: #8e949c;
    --gray-light: #d9dce0;
    --block: #eceef1;
    --paper: #ffffff;
    --bg: #e9eaec;
    --ink: #4a4f57;
  }
  * { box-sizing: border-box; margin: 0; padding: 0; }
  html, body { width: 1200px; height: 310px; overflow: hidden; background: var(--bg); font-family: "Montserrat", Arial, sans-serif; color: var(--ink); }
  .canvas { position: relative; width: 1200px; height: 310px; }
  .piece { position: absolute; background: var(--paper); box-shadow: 0 1px 3px rgba(0,0,0,.18); overflow: hidden; }
  .caption { position: absolute; font-size: 5px; line-height: 6px; color: var(--gray); text-align: center; white-space: nowrap; }
  .logo { display: flex; align-items: center; gap: 3px; color: var(--navy); font-weight: 800; letter-spacing: .5px; white-space: nowrap; }
  .logo .mark { background: var(--navy); display: block; flex: none; }
  .brand-block { position: absolute; left: 8px; top: 30px; }
  .brand-block .logo { font-size: 40px; gap: 6px; }
  .brand-block .logo .mark { width: 26px; height: 26px; }
  .brand-block .tag { font-size: 6px; color: var(--gray); margin-top: 4px; letter-spacing: .3px; }
  .card { width: 122px; height: 68px; }
  .card .logo { position: absolute; left: 8px; top: 12px; font-size: 14px; }
  .card .logo .mark { width: 9px; height: 9px; }
  .card .info { position: absolute; right: 6px; top: 9px; font-size: 3.6px; line-height: 1.5; text-align: right; white-space: nowrap; }
  .card .info b { font-size: 5px; color: var(--navy); display: block; }
  .card svg { position: absolute; left: 0; bottom: 0; }
  .card.back { background: var(--navy); }
  .card.back .logo { color: #fff; left: 50%; top: 50%; transform: translate(-50%,-50%); }
  .card.back .logo .mark { background: #fff; }
  .card.list .services { position: absolute; left: 8px; top: 10px; font-size: 3.6px; line-height: 1.6; }
  .card.list .logo { left: auto; right: 8px; top: auto; bottom: 20px; }
  .letterhead { width: 200px; height: 270px; top: 12px; }
  .letterhead .logo { position: absolute; left: 14px; top: 14px; font-size: 16px; }
  .letterhead .logo .mark { width: 10px; height: 10px; }
  .letterhead .contact { position: absolute; right: 14px; top: 14px; font-size: 3.6px; line-height: 1.6; text-align: right; white-space: nowrap; }
  .letterhead svg { position: absolute; left: 0; top: 0; }
  .envelope { width: 194px; height: 106px; }
  .envelope .logo { position: absolute; left: 10px; top: 10px; font-size: 12px; }
  .envelope .logo .mark { width: 8px; height: 8px; }
  .envelope .return { position: absolute; left: 10px; top: 28px; font-size: 3.6px; line-height: 1.5; white-space: nowrap; }
  .envelope svg { position: absolute; left: 0; bottom: 0; }
  .env-back { width: 264px; }
</style>
</head>
<body>
<div class="canvas">

  <div class="brand-block">
    <div class="logo"><span class="mark"></span>RLB</div>
    <div class="tag">Hollowbrook Upkeep</div>
  </div>

  <!-- business cards -->
  <div class="piece card" style="left:6px;top:125px;">
    <div class="logo"><span class="mark"></span>RLB</div>
    <div class="info"><b>Dale Vorrinth</b>CEO<br>3187 Tollgate Fern Ct., #412<br>Brennick Falls, OH 44821<br>Dale@HollowbrookUpkeep.com<br>www.hollowbrookupkeep.com</div>
    <svg width="122" height="14" viewBox="0 0 122 14"><path d="M0 8 Q61 0 122 6 V14 H0Z" fill="var(--gray-light)"/><path d="M0 11 Q61 4 122 9 V14 H0Z" fill="var(--navy)"/></svg>
  </div>
  <div class="piece card back" style="left:134px;top:125px;">
    <div class="logo"><span class="mark"></span>RLB</div>
  </div>
  <div class="piece card list" style="left:6px;top:205px;">
    <div class="services">General Facilities Management<br>Build-Outs<br>Carpentry<br>Painting<br>Drywall</div>
    <div class="logo"><span class="mark"></span>RLB</div>
    <svg width="122" height="14" viewBox="0 0 122 14"><path d="M0 11 Q61 4 122 9 V14 H0Z" fill="var(--navy)"/></svg>
  </div>
  <div class="piece card back" style="left:134px;top:205px;">
    <div class="logo"><span class="mark"></span>RLB</div>
  </div>
  <span class="caption" style="left:6px;top:277px;width:122px;">Card Front</span>
  <span class="caption" style="left:134px;top:277px;width:122px;">Card Back</span>

  <!-- letterheads -->
  <div class="piece letterhead" style="left:278px;">
    <svg width="200" height="270" viewBox="0 0 200 270">
      <g fill="var(--block)">
        <rect x="62" y="62" width="52" height="16"/><rect x="92" y="84" width="52" height="16"/>
        <rect x="62" y="106" width="52" height="16"/><rect x="92" y="128" width="52" height="16"/>
        <rect x="62" y="150" width="52" height="16"/><rect x="92" y="172" width="52" height="16"/>
      </g>
      <path d="M0 252 Q100 236 200 246 V270 H0Z" fill="var(--gray-light)"/>
      <path d="M0 258 Q100 244 200 254 V270 H0Z" fill="var(--navy)"/>
    </svg>
    <div class="logo"><span class="mark"></span>RLB</div>
    <div class="contact">3187 Tollgate Fern Ct., #412<br>Brennick Falls, OH 44821<br>Dale@HollowbrookUpkeep.com<br>www.hollowbrookupkeep.com</div>
  </div>
  <div class="piece letterhead" style="left:492px;">
    <svg width="200" height="270" viewBox="0 0 200 270">
      <g fill="var(--block)">
        <rect x="62" y="62" width="52" height="16"/><rect x="92" y="84" width="52" height="16"/>
        <rect x="62" y="106" width="52" height="16"/><rect x="92" y="128" width="52" height="16"/>
        <rect x="62" y="150" width="52" height="16"/><rect x="92" y="172" width="52" height="16"/>
      </g>
      <path d="M0 258 Q100 244 200 254 V270 H0Z" fill="var(--navy)"/>
    </svg>
    <div class="logo" style="left:50%;transform:translateX(-50%);"><span class="mark"></span>RLB</div>
  </div>
  <span class="caption" style="left:278px;top:286px;width:200px;">Letterhead Page 1</span>
  <span class="caption" style="left:492px;top:286px;width:200px;">Letterhead Page 2</span>

  <!-- envelope fronts -->
  <div class="piece envelope" style="left:713px;top:36px;">
    <div class="logo"><span class="mark"></span>RLB</div>
    <div class="return">3187 Tollgate Fern Ct., #412<br>Brennick Falls, OH 44821</div>
    <svg width="194" height="10" viewBox="0 0 194 10"><path d="M0 6 Q97 0 194 4 V10 H0Z" fill="var(--navy)"/></svg>
  </div>
  <div class="piece envelope" style="left:713px;top:178px;">
    <div class="logo"><span class="mark"></span>RLB</div>
    <div class="return">3187 Tollgate Fern Ct., #412<br>Brennick Falls, OH 44821</div>
    <svg width="194" height="10" viewBox="0 0 194 10"><path d="M0 6 Q97 0 194 4 V10 H0Z" fill="var(--navy)"/></svg>
  </div>
  <span class="caption" style="left:713px;top:288px;width:194px;">Envelope Front</span>

  <!-- envelope backs -->
  <div class="piece envelope env-back" style="left:924px;top:24px;height:76px;background:var(--gray);">
    <svg width="264" height="76" viewBox="0 0 264 76" style="top:0;bottom:auto;">
      <path d="M0 0 L132 60 L264 0 V76 H0Z" fill="var(--paper)"/>
    </svg>
    <div class="logo" style="left:50%;top:16px;transform:translateX(-50%);color:#fff;"><span class="mark" style="background:#fff"></span>RLB</div>
  </div>
  <div class="piece envelope env-back" style="left:924px;top:104px;height:76px;background:var(--paper);">
    <svg width="264" height="76" viewBox="0 0 264 76" style="top:0;bottom:auto;">
      <path d="M0 0 H264 L132 56Z" fill="var(--navy)"/>
      <path d="M0 76 L110 40 M264 76 L154 40" stroke="var(--gray-light)" stroke-width="1" fill="none"/>
    </svg>
    <div class="logo" style="left:50%;top:14px;transform:translateX(-50%);color:#fff;"><span class="mark" style="background:#fff"></span>RLB</div>
  </div>
  <div class="piece envelope env-back" style="left:924px;top:192px;height:90px;">
    <svg width="264" height="90" viewBox="0 0 264 90" style="top:0;bottom:auto;">
      <path d="M0 0 L132 46 L264 0" stroke="var(--gray-light)" stroke-width="1.2" fill="none"/>
      <path d="M0 90 L112 40 M264 90 L152 40" stroke="var(--gray-light)" stroke-width="1" fill="none"/>
    </svg>
    <div class="logo" style="left:50%;top:50px;transform:translateX(-50%);"><span class="mark"></span>RLB</div>
  </div>
  <span class="caption" style="left:924px;top:286px;width:264px;">Envelope Back</span>

</div>
</body>
</html>
```